NEED BILLBOARDS FOR LUMIVANCE

we need to redo our billboards for our business. we want to have catchy, great billboards that follow standard billboard design rules. we do breast and body cosmetic surgery in Bakersfield, fresno, and stockton ca. see attached for some tips. i would like something creative, but conservative, but funny. we also won finest of county 18 years in a row and can give you the logo

Target Market(s)

females 21-45

Industry/Entity Type

plastic surgery of the breast and body

Font styles to use
Serif

Requirements
Nice to have
• funny, catchy
Should not have
• pictures of women that are overly exposed

```html
<!DOCTYPE html>
<html lang="en">
<head>
<meta charset="utf-8">
<title>Lumivance Billboard</title>
<link rel="stylesheet" href="https://fonts.googleapis.com/css2?family=Oswald:wght@300;600;700&family=Montserrat:wght@400;700&display=swap">
<style>
  :root {
    --page-bg: #e9ecef;
    --board-white: #ffffff;
    --mist-light: #f4f3f1;
    --mist-mid: #e6e3de;
    --skin-light: #f1ddd0;
    --skin-deep: #d9b39c;
    --fabric: #f3efe6;
    --ink: #2a2a2a;
    --accent-orange: #f39332;
    --logo-red: #e01818;
  }
  * { margin: 0; padding: 0; box-sizing: border-box; }
  html, body {
    width: 1200px;
    height: 905px;
    overflow: hidden;
    background: var(--page-bg);
  }
  .billboard {
    position: absolute;
    left: 30px;
    top: 252px;
    width: 1140px;
    height: 400px;
    background: var(--board-white);
    overflow: hidden;
  }
  .backdrop {
    position: absolute;
    left: 0; top: 0;
    width: 720px; height: 400px;
    background: linear-gradient(100deg, var(--mist-light) 0%, var(--mist-mid) 55%, var(--mist-light) 100%);
  }
  .model-photo {
    position: absolute;
    left: 430px; top: 30px;
    width: 290px; height: 370px;
    background: linear-gradient(180deg, var(--skin-light) 0%, var(--skin-deep) 45%, var(--fabric) 70%, var(--skin-light) 100%);
  }
  .logo-frame {
    position: absolute;
    left: 100px; top: 70px;
    width: 200px; height: 200px;
    border: 3px solid var(--logo-red);
    display: flex;
    align-items: center;
    justify-content: center;
  }
  .logo-text {
    font-family: "Oswald", sans-serif;
    font-weight: 300;
    font-size: 80px;
    line-height: 0.95;
    color: var(--ink);
    text-align: left;
    letter-spacing: 1px;
  }
  .service-note {
    position: absolute;
    left: 40px; top: 318px;
    font-family: "Montserrat", sans-serif;
    font-size: 14px;
    color: var(--ink);
    line-height: 1.45;
  }
  .service-note .cities { font-weight: 700; }
  .headline {
    position: absolute;
    left: 735px; top: 68px;
    width: 390px;
    font-family: "Oswald", sans-serif;
    font-weight: 700;
    font-size: 58px;
    line-height: 1.0;
    letter-spacing: -0.5px;
    text-transform: uppercase;
    color: var(--ink);
    text-align: center;
    white-space: nowrap;
  }
  .headline .accent { color: var(--accent-orange); }
  .smile {
    position: absolute;
    left: 870px; top: 258px;
    width: 120px; height: 40px;
  }
  .award-band {
    position: absolute;
    left: 720px; top: 348px;
    width: 420px; height: 52px;
    background: var(--accent-orange);
    display: flex;
    align-items: center;
    justify-content: center;
    font-family: "Montserrat", sans-serif;
    font-weight: 700;
    font-size: 17px;
    color: var(--board-white);
    text-transform: uppercase;
  }
</style>
</head>
<body>
  <main class="billboard">
    <div class="backdrop"></div>
    <div class="model-photo" role="img" aria-label="Photo of a woman's torso in a white crop top wrapped in flowing white fabric"></div>

    <div class="logo-frame">
      <div class="logo-text">LOGO<br>HERE</div>
    </div>

    <p class="service-note">
      We do breast and body cosmetic surgery in<br>
      <span class="cities">BAKERSFIELD, FRESNO, AND STOCKTON CA.</span>
    </p>

    <h1 class="headline">
      <span class="accent">Shape your</span><br>
      Body to make<br>
      your smile
    </h1>

    <svg class="smile" viewBox="0 0 120 40" aria-hidden="true">
      <path d="M8 10 Q60 55 112 10" fill="none" stroke="#2a2a2a" stroke-width="2.5" stroke-linecap="round"/>
      <path d="M4 6 L12 14" stroke="#2a2a2a" stroke-width="2.5" stroke-linecap="round"/>
      <path d="M116 6 L108 14" stroke="#2a2a2a" stroke-width="2.5" stroke-linecap="round"/>
    </svg>

    <div class="award-band">Finest of county 18 years</div>
  </main>
</body>
</html>
```